Retail Jewelry Business Card Design Project

We are in need of a new business card design for a retail jewelry store. This store is in the business of fine jewelry including but not specific to bridal jewelry, diamonds, designer jewelry and watches.

This store has been in business for 20 years but continues to strive for a modern professional appeal. The main colors use for this business are a royal blue, white and silver.

Target Market(s)

Target market is ages 18-50

Industry/Entity Type

Jewelry

Requirements
Must have
• Sales Person Name
Sales Person Email Address

Store Address
Store Phone
Website

Standard business card size. No odd shapes or sizes.
Nice to have
• Overall modern feel for card.

We have thought that a design with a nice feature of the logo on the back of the card would be nice but open to ideas.
Should not have
• No specific images of jewelry should be used.

```html
<!DOCTYPE html>
<html lang="en">
<head>
<meta charset="utf-8">
<title>Hale Brennan Fine Jewelry – Business Cards</title>
<link href="https://fonts.googleapis.com/css2?family=Tinos:ital,wght@0,400;0,700;1,700&display=swap" rel="stylesheet">
<style>
  :root {
    --stage: #000000;
    --royal-deep: #0f0a4e;
    --royal-mid: #1c1870;
    --royal-glow: #2f2f98;
    --white: #ffffff;
    --silver-light: #f4f4f4;
    --silver: #d9d9dc;
    --logo-blue: #2a2488;
  }
  html, body {
    margin: 0;
    width: 1200px;
    height: 1200px;
    overflow: hidden;
    background: var(--stage);
  }
  .canvas {
    position: relative;
    width: 1200px;
    height: 1200px;
    font-family: "Tinos", "Times New Roman", serif;
  }
  .card {
    position: absolute;
    top: 456px;
    width: 535px;
    height: 305px;
    overflow: hidden;
  }
  .card--front {
    left: 46px;
    background: linear-gradient(135deg, var(--royal-glow) 0%, var(--royal-mid) 45%, var(--royal-deep) 100%);
  }
  .card--back {
    left: 618px;
    background: radial-gradient(ellipse 60% 75% at 50% 30%, var(--royal-glow) 0%, var(--royal-mid) 55%, var(--royal-deep) 100%);
  }
  .front-panel {
    position: absolute;
    inset: 0;
    width: 535px;
    height: 305px;
  }
  .front-brand {
    position: absolute;
    left: 20px;
    width: 300px;
    top: 205px;
    text-align: center;
    color: var(--logo-blue);
    font-weight: 700;
    line-height: 1.1;
  }
  .front-brand__name { font-size: 34px; display: block; }
  .front-brand__line { font-size: 18px; letter-spacing: 2px; text-transform: uppercase; display: block; margin-top: 6px; }
  .contact {
    position: absolute;
    right: 24px;
    top: 152px;
    text-align: right;
    color: var(--white);
  }
  .contact__name { font-size: 18px; font-weight: 700; margin: 0 0 14px; }
  .contact__address { font-size: 15px; line-height: 21px; margin: 0 0 9px; }
  .contact__email { font-size: 15px; line-height: 20px; margin: 0; }
  .contact__web { font-size: 14px; font-weight: 700; font-style: italic; margin: 0; }
  .back-brand {
    position: absolute;
    left: 0;
    right: 0;
    top: 88px;
    text-align: center;
    color: var(--white);
    font-weight: 700;
    line-height: 1;
  }
  .back-brand__name { display: block; font-size: 56px; }
  .back-brand__line { display: block; font-size: 26px; letter-spacing: 3px; text-transform: uppercase; margin-top: 22px; }
</style>
</head>
<body>
<main class="canvas">
  <section class="card card--front" aria-label="Business card front">
    <svg class="front-panel" viewBox="0 0 535 305" aria-hidden="true">
      <defs>
        <linearGradient id="silverPanel" x1="0" y1="0" x2="1" y2="1">
          <stop offset="0" stop-color="#ffffff"/>
          <stop offset="0.6" stop-color="#eeeeef"/>
          <stop offset="1" stop-color="#d6d6da"/>
        </linearGradient>
      </defs>
      <path d="M0 0 H240 C285 40 318 110 316 170 C314 230 290 270 262 305 H0 Z" fill="url(#silverPanel)"/>
    </svg>
    <div class="front-brand">
      <span class="front-brand__name">Hale Brennan</span>
      <span class="front-brand__line">Fine Jewelry</span>
    </div>
    <div class="contact">
      <p class="contact__name">Marcus Hale Brennan</p>
      <p class="contact__address">2280 Larkspur Avenue<br>Bayview, FL 32590</p>
      <p class="contact__email">marcus@halebrennanjewelry.com</p>
      <p class="contact__web">www.halebrennanjewelry.com</p>
    </div>
  </section>

  <section class="card card--back" aria-label="Business card back">
    <div class="back-brand">
      <span class="back-brand__name">Hale Brennan</span>
      <span class="back-brand__line">Fine Jewelry</span>
    </div>
  </section>
</main>
</body>
</html>
```